Landing Page

basically our company has as an strategy to sell our subscription product a set os pages normally in 4 steps
1 - We show that the "customer" will win a prizze
2 - We show some advantages that we have as a company
3 - We show another prizze
4 - We explain that to gain all itens they should make a subscription with a HUGE discount
What do we need?
1 - a new proposal for our set of landing pages
2 - responsive layout for all pages
3 - ideas that can increase our conversion rates
Examples:
http://www.descubravantagens.com/
http://www.descubravantagens.com/vistacam/index.php
http://www.descubravantagens.com/brightdeals/index.php
http://www.descubravantagens.com/v2/index.php
http://atendimentogeral.avaliamos.org.br/index.aspx?prm_id_c=KXR27004
http://www.premiavela.com.br/br_tmk_pro_vsi_int_1.asp?mktcode=TMQW72
https://www.bridgeloop480.info/seq2012/twosteps/pt_br/b2013/index.html?lang=brpt_br&project=TwoSteps&codeprom=FJUB4702&tmpl=b2013&cn=AB11CD22-33EF-4A5B-8C6D-7E8F9A0B1C2D#1
https://atendimentogeral.avaliamos.org.br/step_03.aspx
It Company

```html
<!DOCTYPE html>
<html lang="en">
<head>
<meta charset="utf-8">
<title>Avaliamos – Landing Page</title>
<link href="https://fonts.googleapis.com/css2?family=Open+Sans:wght@300;400;600;700;800&display=swap" rel="stylesheet">
<style>
:root{
  --green:#80bd01;
  --green-dark:#0b5a2a;
  --text:#555;
  --muted:#777;
  --line:#e2e2e2;
  --white:#fff;
}
*{box-sizing:border-box;margin:0;padding:0}
html,body{width:949px;height:1200px;overflow:hidden;background:var(--white)}
body{font-family:"Open Sans",Arial,sans-serif;color:var(--text);position:relative}
.abs{position:absolute}

.logo{left:51px;top:30px;font-size:31px;font-weight:800;color:var(--green-dark);letter-spacing:-.5px}
.nav{right:78px;top:47px;display:flex;list-style:none}
.nav li{font-size:13.5px;color:var(--green-dark);padding:0 16px;border-left:1px solid #ccc;line-height:18px}
.nav li:first-child{border-left:none}
.nav li:last-child{padding-right:0}

.hero-photo{left:8px;top:76px;width:784px;height:372px;
  background:
    linear-gradient(180deg,rgba(255,255,255,.85) 0%,rgba(255,255,255,.25) 35%,rgba(255,255,255,0) 60%),
    linear-gradient(90deg,#f6f1ec 0%,#e9ddd0 8%,#d8c7b2 18%,#ece4da 26%,#d6c3a6 36%,#c8c2b8 46%,#b9b0a2 52%,#8e8f93 62%,#a8a29a 70%,#cdbb9f 80%,#eee8e0 90%,#f8f6f3 100%)}
.band{left:0;top:448px;width:949px;height:60px;background:linear-gradient(180deg,#f0f0f0,#fff)}

.signup{left:607px;top:114px;width:271px;height:308px;background:var(--green);border-radius:4px;padding:26px 26px 0}
.signup h2{font-weight:300;font-size:22px;color:var(--white);line-height:24px}
.signup .lead{font-size:9.5px;font-weight:600;color:var(--white);margin-bottom:12px}
.field{height:25px;background:var(--white);border-radius:3px;border:1px solid #d9d9d9;font-size:10.5px;color:#888;padding:5px 10px;margin-bottom:7px}
.field.select{width:108px;position:relative}
.field.select::after{content:"";position:absolute;right:8px;top:10px;border:5px solid transparent;border-top-color:#555;border-bottom:none}
.field.wide{width:216px}
.signup .note{font-size:9.3px;font-weight:300;color:var(--white);line-height:15px;margin:3px 0 6px;width:216px}
.signup .cta{width:218px;height:37px;background:linear-gradient(180deg,#0d7a35,#075a24);border-radius:3px;color:var(--white);font-size:16px;text-align:center;line-height:37px}

.section-title{left:0;top:475px;width:949px;text-align:center;font-size:24px;font-weight:400;color:var(--green-dark)}
.card{top:524px;width:207px;height:204px;border:1px solid var(--line);border-radius:3px;background:linear-gradient(180deg,#fff 70%,#f6f6f6);text-align:center}
.card .art{width:92px;height:92px;margin:13px auto 0;border-radius:6px}
.card h3{font-weight:400;font-size:21px;color:var(--green);margin-top:14px;line-height:26px}
.card p{font-size:10.5px;color:var(--muted);line-height:15px;margin-top:2px}

.track{left:66px;top:778px;width:816px;height:2px;background:#ddd}
.step-label{top:743px;width:80px;text-align:center;font-size:16px;color:#666}
.dot{top:773px;width:13px;height:13px;border-radius:50%;border:2px solid var(--green);background:var(--white)}
.dot.on{background:var(--green)}

.col-title{top:826px;font-size:22px;font-weight:300;color:#555}
.col-img{top:859px;width:247px;height:96px}
.col-sub{top:960px;font-size:13.5px;font-weight:400;color:#555}
.col-text{top:983px;width:240px;font-size:9.3px;line-height:16.6px;color:var(--muted)}
.divider{top:834px;width:1px;height:227px;background:var(--line)}

.post-thumb{width:80px;height:72px;border:3px solid #fff;box-shadow:0 0 2px #bbb}
.post-title{font-size:11.5px;font-weight:600;color:#555;line-height:17px;width:160px}
.post-text{font-size:9.3px;color:var(--muted);line-height:16.6px;width:160px}
.more{font-size:9.3px;font-weight:700;color:#444}

.footer{left:0;top:1104px;width:949px;height:96px;background:var(--green);border-top:2px solid #9bcc35}
.footer .links{left:56px;top:24px;font-size:12.5px;font-weight:600;color:var(--white);word-spacing:2px}
.footer .copy{left:56px;top:50px;font-size:10.5px;color:var(--white)}
.social{top:28px;width:25px;height:25px;border-radius:50%;background:var(--white)}
</style>
</head>
<body>

<div class="abs logo">AVALIAMOS</div>
<ul class="abs nav">
  <li>HOME</li><li>ABOUT</li><li>SERVICE</li><li>SUPPORT</li><li>MEMBER</li><li>CONTACT</li>
</ul>

<div class="abs band"></div>
<div class="abs hero-photo" role="img" aria-label="Photo of a smiling group of six people in light shirts and sweaters standing together on a white background"></div>

<form class="abs signup">
  <h2>BECOME A MEMBER</h2>
  <div class="lead">Etiam eu urna Sed porta Suspendisse quam</div>
  <div class="field select">Sex</div>
  <div class="field wide">Your name</div>
  <div class="field wide">Username</div>
  <div class="field wide">Email address</div>
  <p class="note">Entendo que ao me inscrever, passarei a receber ofertas de produtos e serviços da AVALIAMOS e parceiros.</p>
  <div class="cta">PROXIMO PASSO</div>
</form>

<h2 class="abs section-title">How to Selling Product</h2>

<div class="abs card" style="left:49px">
  <div class="art" role="img" aria-label="Red gift box with gold ribbon" style="background:linear-gradient(135deg,#e8312a,#b5140f)"></div>
  <h3>Win Prices</h3>
  <p>We show that the "customer"<br>will win a prize</p>
</div>
<div class="abs card" style="left:263px">
  <div class="art" role="img" aria-label="Blue award rosette with ribbons" style="background:linear-gradient(135deg,#2556b8,#163c8c)"></div>
  <h3>Show Advantage</h3>
  <p>We show some advantages<br>that we have as a company</p>
</div>
<div class="abs card" style="left:478px">
  <div class="art" role="img" aria-label="Two golden gift boxes with red bows" style="background:linear-gradient(135deg,#f7c34a,#e08a1a)"></div>
  <h3>More Prize</h3>
  <p>We show another prize</p>
</div>
<div class="abs card" style="left:693px">
  <div class="art" role="img" aria-label="Orange shopping bag with percent sign" style="background:linear-gradient(135deg,#ffc72c,#f08a00)"></div>
  <h3 style="margin-top:4px">HUGE discount</h3>
  <p>We explain that to gain all items<br>they should make a subscription<br>with a HUGE discount</p>
</div>

<div class="abs track"></div>
<div class="abs step-label" style="left:112px">Step 1</div>
<div class="abs step-label" style="left:327px">Step 2</div>
<div class="abs step-label" style="left:543px">Step 3</div>
<div class="abs step-label" style="left:757px">Step 4</div>
<div class="abs dot on" style="left:146px"></div>
<div class="abs dot" style="left:361px"></div>
<div class="abs dot" style="left:577px"></div>
<div class="abs dot" style="left:791px"></div>

<h3 class="abs col-title" style="left:66px">What We Do</h3>
<div class="abs col-img" style="left:66px;background:linear-gradient(90deg,#b8324a,#3a2a1e,#c8426a)" role="img" aria-label="Photo of three friends exchanging holiday gifts"></div>
<div class="abs col-sub" style="left:66px">Donec scelerisque leo ac risus.</div>
<p class="abs col-text" style="left:66px">Praesent sit amet est. In dictum, dolor eu dictum porttitor, enim felis viverra mi, eget luctus massa purus quis odio. Etiam nulla massa, pharetra facilisis, volutpat in, imperdiet sit amet, sem.</p>

<div class="abs divider" style="left:332px"></div>

<h3 class="abs col-title" style="left:353px">Our Products</h3>
<div class="abs col-img" style="left:351px;background:linear-gradient(90deg,#8fae86,#d9d4cc,#6b5044)" role="img" aria-label="Photo of a woman using a laptop near a festive tree"></div>
<div class="abs col-sub" style="left:355px">Donec scelerisque leo ac risus.</div>
<p class="abs col-text" style="left:355px">Praesent sit amet est. In dictum, dolor eu dictum porttitor, enim felis viverra mi, eget luctus massa purus quis odio. Etiam nulla massa, pharetra facilisis, volutpat in, imperdiet sit amet, sem.</p>

<div class="abs divider" style="left:619px"></div>

<h3 class="abs col-title" style="left:642px">Recent Blog Post</h3>
<div class="abs post-thumb" style="left:642px;top:864px;background:linear-gradient(135deg,#f2a23a,#7fc3dc)" role="img" aria-label="Summer guide booklet cover illustration"></div>
<div class="abs post-title" style="left:736px;top:862px">Phasellus felis dolor sceleris-que a tempus eget</div>
<div class="abs post-text" style="left:736px;top:898px">Nunc tempus felis vitae urna. Viva-mus porttitor purus nisi</div>
<div class="abs more" style="left:736px;top:934px">LEARN MORE</div>

<div class="abs post-thumb" style="left:642px;top:974px;background:linear-gradient(135deg,#2a2a2a,#d8d8d8)" role="img" aria-label="Tablet showing a website screen"></div>
<div class="abs post-title" style="left:738px;top:971px">Praesent elementum elit</div>
<div class="abs post-text" style="left:738px;top:990px">Nunc tempus felis vitae urna. Viva-mus porttitor purus nisi</div>
<div class="abs more" style="left:738px;top:1026px">LEARN MORE</div>

<footer class="abs footer">
  <div class="abs links">HOME &nbsp;|&nbsp; ABOUT &nbsp;|&nbsp; SERVICE &nbsp;|&nbsp; SUPPORT &nbsp;|&nbsp; MEMBER &nbsp;|&nbsp; CONTACT</div>
  <div class="abs copy">© 2013 Company Name. &nbsp;All right reserved. &nbsp;Term of Use</div>
  <div class="abs social" style="left:786px"></div>
  <div class="abs social" style="left:814px"></div>
  <div class="abs social" style="left:842px"></div>
  <div class="abs social" style="left:870px"></div>
</footer>

</body>
</html>
```